Birchford Realty Business Card

Business Card:

Somewhere on front of card, please include Broker License Number: 5839162

Website is BirchfordRealty.example

Address is:
7218 Crestover Ave E
Saginaw, MI 48271

I'll let you use creative freedom on the rest; we obviously need Name, Title, Email (@BirchfordRealty.example), Office Phone, Cell Phone.

Don't want any special die-cutting, just a standard size business card.

On the back, include a place for the date and time of an appointment to be written in pen.

Requirements
Must have
• Our logo, attached to email.

```html
<!DOCTYPE html>
<html lang="en">
<head>
<meta charset="utf-8">
<title>Birchford Realty Business Card</title>
<link href="https://fonts.googleapis.com/css2?family=Open+Sans:wght@400;600;700&display=swap" rel="stylesheet">
<style>
  :root {
    --navy: #2a2a86;
    --navy-deep: #1f1f6e;
    --navy-light: #5b5fb0;
    --silver: #c4c6cc;
    --silver-dark: #9a9ca4;
    --paper: #ffffff;
    --backdrop: #ecebe8;
    --ink-soft: #dfe0f3;
  }
  * { margin: 0; padding: 0; box-sizing: border-box; }
  html, body { width: 1200px; height: 913px; overflow: hidden; }
  body {
    background: var(--backdrop);
    font-family: "Open Sans", sans-serif;
    position: relative;
  }
  .card {
    position: absolute;
    width: 530px;
    height: 303px;
    background: var(--paper);
    border-radius: 16px;
    overflow: hidden;
    box-shadow: 0 6px 18px rgba(0,0,0,0.18);
  }
  .card-front { left: 70px; top: 110px; }
  .card-back { left: 600px; top: 500px; }
  .card-shapes { position: absolute; inset: 0; width: 100%; height: 100%; }

  .brand {
    position: absolute;
    color: var(--navy);
    font-weight: 700;
    font-size: 28px;
    letter-spacing: -0.3px;
    white-space: nowrap;
  }
  .card-front .brand { left: 32px; top: 158px; }
  .card-back .brand { left: 60px; top: 42px; font-size: 30px; }

  .license {
    position: absolute;
    left: 34px;
    top: 200px;
    font-size: 11px;
    font-weight: 600;
    color: var(--silver-dark);
    letter-spacing: 0.3px;
    white-space: nowrap;
  }

  .contact {
    position: absolute;
    right: 28px;
    top: 30px;
    text-align: right;
    color: var(--paper);
  }
  .contact-name { font-weight: 700; font-size: 19px; letter-spacing: 0.3px; }
  .contact-title { font-size: 11px; color: var(--ink-soft); letter-spacing: 0.5px; margin-bottom: 14px; }
  .contact-address { font-size: 12px; line-height: 1.45; margin-bottom: 10px; }
  .contact-line {
    display: flex; justify-content: flex-end; align-items: center; gap: 6px;
    font-size: 12px; line-height: 1.6;
  }
  .contact-line svg { width: 11px; height: 11px; flex: none; }

  .appointment {
    position: absolute;
    left: 40px; right: 40px; top: 112px;
    color: var(--navy);
    font-size: 13px;
    font-weight: 600;
  }
  .appointment-label { text-align: center; margin-bottom: 16px; }
  .appointment-row { display: flex; align-items: flex-end; gap: 6px; white-space: nowrap; }
  .fill-line { flex: 1; border-bottom: 1.5px dotted var(--navy); height: 14px; }
  .fill-line.time { flex: 0.9; }
</style>
</head>
<body>

<section class="card card-front" aria-label="Card front">
  <svg class="card-shapes" viewBox="0 0 530 303" preserveAspectRatio="none" aria-hidden="true">
    <defs>
      <linearGradient id="frontBlue" x1="0" y1="0" x2="0" y2="1">
        <stop offset="0" stop-color="#5b5fb0"/>
        <stop offset="0.5" stop-color="#2f2f8c"/>
        <stop offset="1" stop-color="#1f1f6e"/>
      </linearGradient>
    </defs>
    <path d="M240 0 C300 70 330 190 300 303 L530 303 L530 0 Z" fill="url(#frontBlue)"/>
    <path d="M222 0 C285 70 312 190 282 303" fill="none" stroke="var(--silver)" stroke-width="6"/>
    <path d="M232 0 C294 70 322 190 292 303" fill="none" stroke="var(--navy-light)" stroke-width="3"/>
  </svg>
  <div class="brand">Birchford Realty</div>
  <div class="license">Broker License #5839162</div>
  <div class="contact">
    <div class="contact-name">DANA WHITLOW</div>
    <div class="contact-title">OWNER</div>
    <div class="contact-address">7218 Crestover Ave E<br>Saginaw, MI 48271</div>
    <div class="contact-line">+1 989-555-0142
      <svg viewBox="0 0 12 12"><path d="M3 1l2 2.5-1.2 1.2a7 7 0 0 0 3.5 3.5L8.5 7 11 9l-1.2 1.8C6 11 1 6 1.2 2.2Z" fill="#fff"/></svg>
    </div>
    <div class="contact-line">+1 989-555-0187
      <svg viewBox="0 0 12 12"><rect x="3" y="0.8" width="6" height="10.4" rx="1" fill="none" stroke="#fff" stroke-width="1.2"/><circle cx="6" cy="9.3" r="0.7" fill="#fff"/></svg>
    </div>
    <div class="contact-line">info@BirchfordRealty.example
      <svg viewBox="0 0 12 12"><rect x="1" y="2.5" width="10" height="7" fill="none" stroke="#fff" stroke-width="1.2"/><path d="M1 2.5l5 4 5-4" fill="none" stroke="#fff" stroke-width="1.2"/></svg>
    </div>
    <div class="contact-line">www.BirchfordRealty.example
      <svg viewBox="0 0 12 12"><circle cx="6" cy="6" r="5" fill="none" stroke="#fff" stroke-width="1.1"/><ellipse cx="6" cy="6" rx="2.2" ry="5" fill="none" stroke="#fff" stroke-width="1"/><path d="M1 6h10" stroke="#fff" stroke-width="1"/></svg>
    </div>
  </div>
</section>

<section class="card card-back" aria-label="Card back">
  <svg class="card-shapes" viewBox="0 0 530 303" preserveAspectRatio="none" aria-hidden="true">
    <defs>
      <linearGradient id="backBlue" x1="0" y1="0" x2="1" y2="1">
        <stop offset="0" stop-color="#3b3c9c"/>
        <stop offset="1" stop-color="#1f1f6e"/>
      </linearGradient>
    </defs>
    <path d="M0 303 L0 280 C200 272 420 232 530 172 L530 303 Z" fill="url(#backBlue)"/>
    <path d="M0 272 C200 264 420 224 530 164" fill="none" stroke="var(--silver)" stroke-width="7"/>
  </svg>
  <div class="brand">Birchford Realty</div>
  <div class="appointment">
    <div class="appointment-label">Appointment:</div>
    <div class="appointment-row">
      <span>Date:</span><span class="fill-line"></span><span>, Time:</span><span class="fill-line time"></span>
    </div>
  </div>
</section>

</body>
</html>
```